Web design required

1-We need a web design for existing company based in New Zealand
2-We build residential house and light commercial
3-We has in-house designer which allow us can provide interior design
4-We modeling project before site construction, which enable both client and construction team to visually analysis whole project,

Target Market(s)

middle class residential house market
Ref: http://www.brambleworthbuilders.co.nz/

Industry/Entity Type

Construction Company

Number of Pages Required

1 page

Font styles to use
Sans Serif
Other font styles liked:
• Such as : Central Gothic or similar which has more design taste

Colors

Designer to choose colors to be used in the design.

Requirements
Must have
• Front sheet, contact information, sample project

```html
<!DOCTYPE html>
<html lang="en">
<head>
<meta charset="utf-8">
<title>Halcyon Homes</title>
<link rel="stylesheet" href="https://fonts.googleapis.com/css2?family=Oswald:wght@500;600&family=Roboto:wght@300;400;500;700&display=swap">
<style>
  :root {
    --brand-blue: #1f8df0;
    --brand-bright: #1a90ff;
    --ink: #2b3340;
    --white: #ffffff;
    --nav-black: #0b0b0d;
    --field: #1f5fa8;
    --footer-text: #7a808a;
  }
  * { box-sizing: border-box; margin: 0; padding: 0; }
  html, body { width: 1200px; height: 2508px; overflow: hidden; }
  body { font-family: "Roboto", Arial, sans-serif; color: var(--white); background: var(--white); position: relative; }

  /* Header */
  .site-header { position: absolute; top: 0; left: 0; width: 1200px; height: 160px; background: var(--white); }
  .brand { position: absolute; left: 60px; top: 38px; display: flex; align-items: center; gap: 16px; }
  .brand-square { width: 70px; height: 70px; background: var(--brand-blue); }
  .brand-name { font-family: "Roboto", Arial, sans-serif; font-weight: 500; font-size: 42px; color: var(--ink); letter-spacing: 1px; }
  .social { position: absolute; right: 52px; top: 28px; display: flex; gap: 10px; }
  .social span { width: 30px; height: 30px; background: var(--brand-blue); border-radius: 4px; }

  .main-nav { position: absolute; left: 240px; top: 120px; width: 720px; height: 112px; background: var(--nav-black); z-index: 3;
    display: flex; justify-content: center; align-items: center; gap: 44px; }
  .main-nav a { font-family: "Roboto", Arial, sans-serif; font-size: 30px; font-weight: 400; color: var(--white); text-decoration: none; position: relative; padding-bottom: 10px; }
  .main-nav a.active::after { content: ""; position: absolute; left: 0; right: 0; bottom: -2px; height: 5px; background: var(--brand-blue); }

  /* Hero */
  .hero { position: absolute; top: 160px; left: 0; width: 1200px; height: 680px; overflow: hidden; }
  .hero-photo { position: absolute; inset: 0;
    background:
      radial-gradient(ellipse at 70% 55%, rgba(255,190,110,.55), transparent 40%),
      linear-gradient(180deg, #4a5560 0%, #6d7378 35%, #5a5a55 60%, #3e5a2c 78%, #4f7a36 100%); }
  .hero-copy { position: absolute; left: 248px; top: 236px; width: 620px; }
  .hero-title { font-family: "Oswald", "Arial Narrow", sans-serif; font-weight: 600; font-size: 32px; line-height: 42px; text-transform: uppercase; color: var(--white); white-space: nowrap; }
  .hero-title em { font-style: normal; color: var(--brand-blue); }
  .hero-text { margin-top: 16px; font-size: 13px; line-height: 18px; font-weight: 300; width: 460px; }
  .hero-controls { margin-top: 26px; display: flex; gap: 6px; }
  .hero-controls span { width: 44px; height: 40px; background: #1b2026; display: flex; align-items: center; justify-content: center; }
  .hero-controls span.on { background: var(--brand-blue); }
  .scroll-cue { position: absolute; left: 586px; top: 570px; width: 28px; height: 28px; border: 2px solid var(--white); border-radius: 4px; display: flex; align-items: center; justify-content: center; }

  /* Works */
  .works { position: absolute; top: 840px; left: 0; width: 1200px; height: 920px; overflow: hidden; }
  .works-backdrop { position: absolute; inset: 0;
    background: linear-gradient(180deg, #0a2a6e 0%, #163f8c 45%, #2457a8 70%, #0f2e68 100%); }
  .section-title { position: absolute; left: 0; width: 1200px; text-align: center; font-size: 34px; font-weight: 400; letter-spacing: 1px; color: var(--white); }
  .works .section-title { top: 36px; }
  .works-grid { position: absolute; left: 240px; top: 132px; width: 720px; height: 676px; background: #0a1a38; border: 4px solid #0a1a38;
    display: grid; grid-template-columns: 1fr 1fr; grid-template-rows: 1fr 1fr 48px; gap: 6px; }
  .work-card { background: #0e1f3f; display: flex; flex-direction: column; }
  .work-photo { flex: 0 0 214px; }
  .work-caption { padding: 8px 10px; font-size: 11px; line-height: 15px; font-weight: 300; color: #dfe7f3; }
  .photo-brick { background: linear-gradient(180deg, #7fb2e0 0%, #b9d4ea 40%, #8a5a44 55%, #6a4434 75%, #4f8a34 100%); }
  .photo-timber { background: linear-gradient(180deg, #8cb8e2 0%, #c6d8ea 38%, #8b6a52 55%, #6d5242 76%, #5a8c3c 100%); }
  .photo-living { background: linear-gradient(180deg, #e8e6e0 0%, #d8d2c6 45%, #b8a890 75%, #a69478 100%); }
  .photo-lounge { background: linear-gradient(180deg, #f2f1ee 0%, #e6e3dc 50%, #c9c0b0 80%, #b6a892 100%); }
  .see-more { grid-column: 1 / span 2; background: var(--brand-blue); display: flex; align-items: center; justify-content: center;
    font-size: 20px; font-weight: 500; color: var(--white); text-decoration: none; }

  /* Contact */
  .contact { position: absolute; top: 1760px; left: 0; width: 1200px; height: 680px; background: var(--brand-bright); }
  .contact .section-title { top: 46px; }
  .contact-form { position: absolute; left: 240px; top: 136px; width: 360px; display: flex; flex-direction: column; gap: 8px; }
  .field { height: 40px; background: var(--field); padding: 9px 10px; font-size: 18px; color: #cfe2f8; }
  .field.message { height: 80px; }
  .office { position: absolute; left: 626px; top: 136px; width: 360px; }
  .office-head { display: flex; align-items: center; gap: 16px; font-size: 26px; }
  .office-text { margin: 8px 0 0 42px; font-size: 25px; line-height: 38px; font-weight: 300; }
  .map { position: absolute; left: 240px; top: 400px; width: 720px; height: 272px;
    background: linear-gradient(135deg, #e9e6df 0%, #dcdad2 45%, #cfe0c4 70%, #e4e2da 100%); }

  /* Footer */
  .site-footer { position: absolute; top: 2440px; left: 0; width: 1200px; height: 68px; background: var(--white);
    display: flex; align-items: center; justify-content: center; font-size: 12px; color: var(--footer-text); }
</style>
</head>
<body>

<header class="site-header">
  <div class="brand">
    <span class="brand-square"></span>
    <span class="brand-name">HALCYON HOMES</span>
  </div>
  <div class="social" aria-label="Social links">
    <span></span><span></span><span></span>
  </div>
</header>

<nav class="main-nav">
  <a href="#home" class="active">HOME</a>
  <a href="#works">WORKS</a>
  <a href="#contact">CONTACT</a>
</nav>

<section class="hero" id="home">
  <div class="hero-photo" role="img" aria-label="Modern two-storey family home at dusk with lit windows and a green lawn"></div>
  <div class="hero-copy">
    <h1 class="hero-title">Lorem Ipsum is <em>simply dummy</em> text<br>of the printing and typesetting industry.</h1>
    <p class="hero-text">We design, model and build homes for New Zealand families, with in-house interior design and a clear 3D view of every project before work starts on site.</p>
    <div class="hero-controls">
      <span><svg width="14" height="14" viewBox="0 0 14 14"><path d="M9 2 L4 7 L9 12" stroke="#fff" stroke-width="2" fill="none"/></svg></span>
      <span class="on"><svg width="14" height="14" viewBox="0 0 14 14"><path d="M5 2 L10 7 L5 12" stroke="#fff" stroke-width="2" fill="none"/></svg></span>
    </div>
  </div>
  <div class="scroll-cue"><svg width="14" height="14" viewBox="0 0 14 14"><path d="M3 5 L7 9 L11 5" stroke="#fff" stroke-width="2" fill="none"/></svg></div>
</section>

<section class="works" id="works">
  <div class="works-backdrop" role="img" aria-label="Glass apartment towers at twilight in deep blue tones"></div>
  <h2 class="section-title">WORKS</h2>
  <div class="works-grid">
    <article class="work-card">
      <div class="work-photo photo-brick" role="img" aria-label="Brick family home with double garage"></div>
      <p class="work-caption">A four-bedroom brick family home with a double garage, modelled in full before the first footing was poured on site.</p>
    </article>
    <article class="work-card">
      <div class="work-photo photo-timber" role="img" aria-label="Timber and brick residence with front lawn"></div>
      <p class="work-caption">A timber and brick residence on a quiet street, built for a growing family with open living and a sunny rear lawn.</p>
    </article>
    <article class="work-card">
      <div class="work-photo photo-living" role="img" aria-label="Open-plan living room with polished floors"></div>
      <p class="work-caption">An open-plan living room with polished floors and soft light, planned by our in-house designer from layout to finish.</p>
    </article>
    <article class="work-card">
      <div class="work-photo photo-lounge" role="img" aria-label="Bright white lounge interior"></div>
      <p class="work-caption">A calm white lounge with warm timber accents, part of a full interior package delivered alongside the new build.</p>
    </article>
    <a class="see-more" href="#works">SEE MORE WORKS</a>
  </div>
</section>

<section class="contact" id="contact">
  <h2 class="section-title">CONTACT</h2>
  <form class="contact-form">
    <div class="field">Name</div>
    <div class="field">Email</div>
    <div class="field">Subject</div>
    <div class="field message">Message</div>
  </form>
  <div class="office">
    <div class="office-head">
      <svg width="24" height="32" viewBox="0 0 24 32"><path d="M12 0 C5 0 0 5 0 12 C0 21 12 32 12 32 C12 32 24 21 24 12 C24 5 19 0 12 0 Z" fill="#fff"/><circle cx="12" cy="12" r="4.5" fill="#1a90ff"/></svg>
      <span>Head Office</span>
    </div>
    <p class="office-text">Lorem Ipsum is simply dummy text of the printing and industry's standard dummy Harbour Road</p>
  </div>
  <div class="map" role="img" aria-label="Street map showing the head office location"></div>
</section>

<footer class="site-footer">All Rights Reserved</footer>

</body>
</html>
```